Web Design Project - Quiet Harbor Advisors

I have a requirement for a simple website that I can manage and change content myself. I'd like to be able to include and change images frequently.

I run a small consulting firm and focus on the area of small to medium sized business turn around. The premise of the business service is that most small businesses "have a monkey on their back" - a problem they need to solve - for example "a Sales Monkey" where their sales team didn't have a solid process or approach or training or the right people; or "a Finance Monkey" where they needed help with Cash flow management or funding, or "an IT Monkey" where their IT systems aren't supporting their supply chain process or ordering process.

So the whole business is build around building monkey characters to represent specific business problems - thus the name Quiet Harbor Advisors.

This always builds into giving each employee their own Monkey character - mine is an Orangutan and appears on my card and Deon (who is our Lawyer) is a Baboon and his character is on his card. I'd like to see these characters also integrated into the site.

The site need to be pretty simple at this stage:

1. Home Page
2. Services Page
3. Who we are / team page
4. Contact Us page

Due to the nature of the name and the imagery around the business I'd like the site to be engaging and colourful, the language I'll use is accessible, down to earth and customer/solution focused.

Target Market(s)

Small to medium sized enterprises looking for assistance with their business. They will be looking for practical solutions at value for money pricing

Industry/Entity Type

Business Service

Requirements
Nice to have
• I'd like the monkey in the logo to swing.

On the People or team page - each person is to have their own monkey character - for example - my business card shows my monkey character as an Orangutan and Deon's monkey character is a baboon - so as the business grows each new person gets their own monkeys character. So on the people or team page it would be fun to have some kind of jungle scene with the character monkeys placed in there and some descriptor of the person.

```html
<!DOCTYPE html>
<html lang="en">
<head>
<meta charset="utf-8">
<title>Quiet Harbor Advisors – Contact Us</title>
<link rel="stylesheet" href="https://fonts.googleapis.com/css2?family=Comfortaa:wght@300;400;700&family=PT+Sans&display=swap">
<style>
  :root {
    --jungle-dark: #0a5a1a;
    --jungle-light: #3f9a1c;
    --bark: #774200;
    --gold: #d6be00;
    --gold-dark: #a68f00;
    --fur: #dcc600;
    --wood-light: #f2a436;
    --wood-mid: #e08a1c;
    --wood-dark: #b96a10;
    --nav-text: #5e3300;
    --badge: #4a4a4a;
    --rule: #d9c9a3;
    --field: #ffffff;
  }
  * { box-sizing: border-box; margin: 0; padding: 0; }
  html, body { width: 1200px; height: 788px; overflow: hidden; }
  body {
    position: relative;
    font-family: 'Comfortaa', sans-serif;
    color: var(--gold);
  }
  .jungle-backdrop {
    position: absolute; inset: 0;
    background: linear-gradient(115deg, var(--jungle-dark) 0%, var(--jungle-light) 35%, var(--jungle-dark) 55%, var(--jungle-light) 80%, var(--jungle-dark) 100%);
  }
  .page-panel {
    position: absolute; left: 146px; top: 20px; width: 911px; height: 748px;
    background: var(--bark);
    border-radius: 20px;
    border-left: 8px solid var(--gold);
    border-right: 8px solid var(--gold);
    box-shadow: inset 4px 0 0 var(--gold-dark), inset -4px 0 0 var(--gold-dark);
  }
  .brand {
    position: absolute; left: 212px; top: 56px;
    font-size: 40px; line-height: 48px; font-weight: 300; letter-spacing: 1px;
    color: var(--gold);
  }
  .main-nav {
    position: absolute; left: 220px; top: 147px; width: 761px; height: 46px;
    background: linear-gradient(180deg, var(--wood-dark) 0 3px, var(--wood-light) 3px 6px, var(--wood-mid) 6px 40px, var(--wood-light) 40px 43px, var(--wood-dark) 43px);
    display: flex; align-items: center; padding-left: 9px;
  }
  .nav-item {
    font-family: 'PT Sans', sans-serif; font-size: 12.5px; color: var(--nav-text);
    text-decoration: none; height: 31px; line-height: 31px;
    text-align: center; border-right: 1px solid var(--wood-dark);
    white-space: nowrap;
  }
  .nav-item.is-active {
    background: var(--wood-light); border: 1px solid var(--wood-dark);
  }
  .nav-badge {
    height: 31px; display: flex; align-items: center; justify-content: center;
    border-right: 1px solid var(--wood-dark);
  }
  .nav-badge span { display: block; width: 18px; height: 28px; background: var(--badge); border-radius: 6px; }
  .gorilla-art {
    position: absolute; left: 243px; top: 264px; width: 212px; height: 363px;
    background: linear-gradient(160deg, var(--fur) 0%, #efe070 45%, var(--fur) 100%);
    border-radius: 70px 50px 18px 18px;
  }
  .contact-box {
    position: absolute; left: 469px; top: 258px; width: 440px; height: 308px;
    border: 1px solid var(--rule);
    border-top: none;
  }
  .contact-legend {
    position: absolute; left: 469px; top: 258px; width: 440px;
    transform: translateY(-50%);
    display: flex; align-items: center; font-size: 14px; line-height: 18px;
  }
  .contact-legend::before, .contact-legend::after {
    content: ""; flex: 1; border-top: 1px solid var(--rule);
  }
  .contact-legend span { padding: 0 1px; }
  .field-label { position: absolute; font-size: 14px; line-height: 18px; text-align: right; width: 100px; }
  .field {
    position: absolute; background: var(--field);
    border: 1px solid #8a8a8a;
  }
  .send-button {
    position: absolute; left: 635px; top: 446px; width: 107px; height: 19px;
    font-family: Arial, sans-serif; font-size: 14px; line-height: 17px; color: #000;
    background: #efefef; border: 1px solid #999; border-radius: 2px;
  }
  .contact-details {
    position: absolute; left: 469px; top: 484px; width: 440px;
    text-align: center; font-size: 13.5px; line-height: 18px;
  }
  .contact-details strong { font-weight: 700; }
  .footer-rule {
    position: absolute; left: 198px; top: 694px; width: 804px; height: 7px;
    background: linear-gradient(180deg, var(--gold) 0 4px, var(--gold-dark) 4px);
  }
  .copyright {
    position: absolute; left: 146px; width: 911px; top: 728px;
    text-align: center; font-size: 13.5px; line-height: 18px;
  }
</style>
</head>
<body>
  <div class="jungle-backdrop" role="img" aria-label="Jungle leaves pattern with swinging monkeys"></div>
  <div class="page-panel"></div>

  <div class="brand">quiet harbor advisors</div>

  <nav class="main-nav">
    <a class="nav-item" href="#" style="width:101px;">Main Jungle</a>
    <div class="nav-badge" style="width:85px;" role="img" aria-label="Gorilla icon"><span></span></div>
    <a class="nav-item" href="#" style="width:87px;">The Primates</a>
    <div class="nav-badge" style="width:83px;" role="img" aria-label="Gorilla icon"><span></span></div>
    <a class="nav-item is-active" href="#" style="width:87px;">Contact Us</a>
    <div class="nav-badge" style="width:101px;" role="img" aria-label="Gorilla icon"><span></span></div>
    <a class="nav-item" href="#" style="width:116px;">Jungle Services</a>
    <div class="nav-badge" style="width:82px;" role="img" aria-label="Gorilla icon"><span></span></div>
  </nav>

  <div class="gorilla-art" role="img" aria-label="Yellow gorilla illustration standing on all fours"></div>

  <div class="contact-box"></div>
  <div class="contact-legend"><span>Contact Us</span></div>

  <label class="field-label" style="left:529px;top:274px;">Name:</label>
  <div class="field" style="left:632px;top:272px;width:161px;height:22px;"></div>

  <label class="field-label" style="left:527px;top:314px;">Email:</label>
  <div class="field" style="left:630px;top:313px;width:161px;height:22px;"></div>

  <label class="field-label" style="left:516px;top:354px;">Message:</label>
  <div class="field" style="left:619px;top:353px;width:208px;height:73px;"></div>

  <button class="send-button" type="button">Send Message</button>

  <div class="contact-details">
    Call us: <strong>1-800-Your-Number</strong><br>
    Email us: address@youremailaddres<br>
    Address: Level 4 Wren Chambers 28 Linden Street<br>
    Harborton NSW 2000 Australia
  </div>

  <div class="footer-rule"></div>
  <div class="copyright">© 2013 Quiet Harbor Advisors. All Rights Reserved.</div>
</body>
</html>
```